Landfill Gas-to-Renewable Natural Gas business

We have a website ( corvelmetharoutes .com via Net Burrow) that needs to be revamped.

We have three RNG projects in Puerto Rico (Humacao, Ponce, Salinas), that take landfill gas (LFG) and produce renewable liquid natural gas (R-LNG) for companies looking to offset their carbon emissions (footprint). We also produce a renewable carbon dioxide (R-CO2) that can be reused for industrial CO2 purposes. All CO2 is imported to the island, so reusing CO2 on the island further reduces global CO2 emissions. The design should reflect renewables, sustainability, professionalism, safety and experience in this sector.

Sites with RNG examples:
https://www.qx.com/en_us/united-states/home/what-we-do/production-and-operations/tolvane-fuels.html
https://brambleflowco.com/
http://kessfordpower.com/operations/
https://wyndcastle.com/
https://www.tamberhold.com/
https://pexloweco.com/
https://sandmoorbiolines.com/
https://curvetto.com/
https://www.dolvatri.com/renewable-natural-gas/
https://www.haskipowerworks.com/

Renewables Natural Gas, Sustainability,

4 page

• Health, Safety, Environment (HSE) aspect. Industry experience section, about us, photos, landfill gas, LNG, RNG, CO2

```html
<!DOCTYPE html>
<html lang="en">
<head>
<meta charset="utf-8">
<title>Corvel Renewables</title>
<link href="https://fonts.googleapis.com/css2?family=Sora:wght@400;500;600;700&family=DM+Sans:wght@400;500;700&display=swap" rel="stylesheet">
<style>
:root{
  --blue:#0a5cf5;
  --green:#12d36b;
  --ink:#1c1f2a;
  --grey:#5d6272;
  --soft:#eef2f7;
  --dark:#1b1c21;
  --leaf-a:#2f9a4c;
  --leaf-b:#c98e4a;
  --line-art:#c9d6ee;
}
*{box-sizing:border-box;margin:0;padding:0}
html,body{width:1200px;height:1200px;overflow:hidden;background:#fff}
body{position:relative;font-family:"DM Sans",sans-serif;color:var(--ink)}
.abs{position:absolute}
.head{font-family:"Sora",sans-serif}
.ph{position:absolute}

/* ---------- page overview column ---------- */
.overview{position:absolute;left:0;top:0;width:227px;height:1200px;overflow:hidden;background:#fff;border-right:1px solid #e3e6ec}
.overview .topline{left:0;top:0;width:227px;height:2px;background:#222}
.ov-nav{top:12px;left:11px;font-size:3.2px;display:flex;gap:5px;color:var(--ink)}
.ov-logo{top:8px;left:113px;display:flex;align-items:center;gap:3px;font-family:"Sora",sans-serif;font-size:4px;color:#4a5470;line-height:1.05}
.ov-logo i{width:9px;height:9px;border-radius:50%;background:var(--green);display:block}
.ov-btn{top:10px;left:181px;width:25px;height:7px;background:var(--blue);color:#fff;font-size:2.6px;text-align:center;line-height:7px}
.ov-grid{top:11px;left:212px;width:4px;height:4px;border:1px dotted #555}
.ov-hero-title{top:76px;left:22px;font-family:"Sora",sans-serif;font-weight:600;font-size:10px;line-height:11px;color:var(--blue);z-index:2}
.ov-hero-title .g{color:var(--green)}
.ov-arrow{top:113px;left:22px;font-size:9px}
.ov-list{right:13px;text-align:right;font-size:4px;line-height:5px;z-index:2}
.ov-list b{color:var(--blue);font-weight:400}
.ov-label{font-size:2.4px;letter-spacing:.3px;color:var(--grey);font-weight:700;text-transform:uppercase}
.ov-h{font-family:"Sora",sans-serif;font-weight:600;font-size:5.4px;line-height:6.2px}
.ov-small{font-size:2.6px;line-height:3.4px;color:var(--grey)}
.ov-band{left:0;top:276px;width:227px;height:286px;background:var(--soft)}
.ov-marquee{top:285px;left:0;white-space:nowrap;font-family:"Sora",sans-serif;font-weight:600;font-size:28px;color:var(--blue)}
.ov-quote{top:339px;left:24px;width:180px;text-align:center;font-family:"Sora",sans-serif;font-weight:500;font-size:8.3px;line-height:9.4px}
.ov-quote u{color:var(--blue)}
.ov-card{background:#fff;padding:8px 8px}
.ov-stats{top:520px;left:22px;width:182px;display:flex;justify-content:space-between}
.ov-stat{position:relative;width:44px;height:26px;border-right:1px solid #dde2ea}
.ov-stat span{position:absolute;left:4px;top:0;font-family:"Sora",sans-serif;font-size:22px;font-weight:600;color:#dfe5ee;line-height:26px}
.ov-stat em{position:absolute;left:14px;top:10px;font-style:normal;font-size:3.6px;font-weight:700}
.ov-logos{top:669px;left:0;width:227px;height:23px;display:flex;border-top:1px solid #e3e6ec;border-bottom:1px solid #e3e6ec}
.ov-logos div{flex:1;border-right:1px solid #e3e6ec;display:flex;align-items:center;justify-content:center}
.ov-logos i{display:block;width:16px;height:4px;background:#d3d8e0;border-radius:2px}
.ov-faq{left:22px;width:182px}
.ov-faq .row{display:flex;justify-content:space-between;border-bottom:1px solid #e1e4ea;font-size:3.2px;font-weight:700;padding:3px 0}
.ov-blog{left:0;top:932px;width:227px;height:131px;background:var(--soft)}
.ov-cta{left:0;top:1063px;width:227px;height:38px;background:var(--blue)}
.ov-foot{left:0;top:1101px;width:227px;height:99px;background:var(--dark);color:#cfd2da}
.ov-art{background:linear-gradient(150deg,#f5f8fd,#dbe5f5);border:1px solid var(--line-art);border-radius:2px}

/* ---------- main view ---------- */
.main{position:absolute;left:245px;top:0;width:955px;height:1200px;background:#fff}
.nav{position:absolute;top:31px;left:48px;display:flex;gap:20px;font-size:12.6px;font-weight:500;color:var(--ink)}
.brand{position:absolute;top:12px;left:481px;display:flex;align-items:center;gap:9px;font-family:"Sora",sans-serif;font-weight:400;font-size:16.5px;line-height:17.5px;color:#3e4a6a}
.brand i{display:block;width:40px;height:40px;border-radius:50%;background:var(--green)}
.btn-contact{position:absolute;top:22px;left:771px;width:108px;height:34px;background:var(--blue);color:#fff;font-size:10.5px;font-weight:700;display:flex;align-items:center;justify-content:center}
.menu-dots{position:absolute;top:32px;left:905px}
.hero-title{position:absolute;top:303px;left:93px;font-family:"Sora",sans-serif;font-weight:700;font-size:42px;line-height:45px;color:var(--blue);letter-spacing:-1.5px;z-index:2}
.hero-title .g{color:var(--green)}
.hero-arrow{position:absolute;top:466px;left:95px}
.hero-art{left:338px;top:150px;width:398px;height:416px;border-radius:50% 50% 46% 54% / 42% 48% 52% 58%;
  background:radial-gradient(ellipse at 30% 45%, #3fae5b 0%, var(--leaf-a) 38%, rgba(47,154,76,.6) 58%, transparent 72%),
             radial-gradient(ellipse at 74% 62%, var(--leaf-b) 0%, #8aa05e 35%, rgba(201,142,74,.35) 60%, transparent 76%)}
.asterisk{position:absolute;top:256px;left:892px;font-family:"Sora",sans-serif;font-size:38px;font-weight:700;line-height:38px}
.hero-list{position:absolute;right:39px;text-align:right;font-family:"Sora",sans-serif;font-size:18px;line-height:21px;letter-spacing:-.3px;z-index:2}
.hero-list b{font-weight:400;color:var(--blue)}
.welcome{position:absolute;top:638px;left:95px;font-size:9.6px;font-weight:700;letter-spacing:1.6px;color:#3a3f4c}
.intro{position:absolute;top:659px;left:95px;width:420px;font-family:"Sora",sans-serif;font-weight:600;font-size:24px;line-height:27px;letter-spacing:-.3px}
.service{position:absolute;top:767px;width:240px}
.service .art{position:relative;width:130px;height:128px;background:linear-gradient(150deg,#f7f9fd 0%,#e3ebf8 60%,#cfdcf3 100%);border:1px solid var(--line-art);border-radius:6px}
.service h3{margin-top:16px;font-family:"Sora",sans-serif;font-weight:600;font-size:19.5px;line-height:22px;letter-spacing:-.2px}
.service p{margin-top:12px;font-size:12.5px;line-height:19px;color:var(--grey)}
.service ul{margin-top:13px;list-style:none;font-size:12.5px;color:var(--grey)}
.service li{position:relative;padding-left:11px;height:25px}
.service li::before{content:"";position:absolute;left:0;top:6px;width:4px;height:4px;border-radius:50%;background:var(--blue)}
.foot-band{position:absolute;left:0;top:1161px;width:955px;height:39px;background:#f0f3f7}
</style>
</head>
<body>

<!-- ===== Full page overview ===== -->
<section class="overview">
  <div class="abs topline"></div>
  <nav class="abs ov-nav"><span>Home</span><span>About Us</span><span>Landfill Gas</span><span>LNG</span><span>RNG</span><span>CO2</span></nav>
  <div class="abs ov-logo"><i></i><span>Corvel<br>Renewables</span></div>
  <div class="abs ov-btn">Contact Us</div>
  <div class="abs ov-grid"></div>

  <div class="ph" role="img" aria-label="Refinery plant set inside a large green leaf beside a landfill site" style="left:76px;top:40px;width:98px;height:97px;border-radius:50%;background:radial-gradient(ellipse at 35% 45%,#3aa757,#2d8a46 45%,rgba(201,142,74,.5) 70%,transparent 78%)"></div>
  <h1 class="abs ov-hero-title">Achieve<br><span class="g">NET-ZERO</span><br>Now</h1>
  <div class="abs ov-arrow">↓</div>
  <div class="abs" style="top:62px;left:210px;font-family:Sora,sans-serif;font-weight:700;font-size:9px">*</div>
  <div class="abs ov-list" style="top:80px"><b>01.</b> Island Sourced<br>Waste-to-Energy</div>
  <div class="abs ov-list" style="top:97px"><b>02.</b> Renewable<br>Natural Gas</div>
  <div class="abs ov-list" style="top:114px"><b>03.</b> ESG positive<br>energy assets</div>

  <div class="abs ov-label" style="top:154px;left:22px">Welcome to Corvel Renewables</div>
  <div class="abs ov-h" style="top:159px;left:22px;width:100px">Transitioning The World To A Zero Carbon Future With Renewable Natural Gas</div>

  <div class="ph ov-art" role="img" aria-label="Line drawing of a landfill gas plant" style="left:22px;top:183px;width:24px;height:30px"></div>
  <div class="ph ov-art" role="img" aria-label="Line drawing of fuel barrels" style="left:84px;top:183px;width:30px;height:30px"></div>
  <div class="ph ov-art" role="img" aria-label="Line drawing of a tanker truck" style="left:146px;top:183px;width:32px;height:30px"></div>
  <div class="abs ov-h" style="top:217px;left:22px;width:58px;font-size:3.6px;line-height:4.4px">Landfill Gas-to-RNG &amp; Electricity Facilities</div>
  <div class="abs ov-h" style="top:217px;left:84px;width:58px;font-size:3.6px;line-height:4.4px">Renewable Natural Gas Production</div>
  <div class="abs ov-h" style="top:217px;left:146px;width:58px;font-size:3.6px;line-height:4.4px">Advanced Waste Processing</div>
  <div class="abs ov-small" style="top:230px;left:22px;width:55px">Natus error sit voluptatem accusantium doloremque laudantium, totam.</div>
  <div class="abs ov-small" style="top:230px;left:84px;width:55px">Natus error sit voluptatem accusantium doloremque laudantium, totam.</div>
  <div class="abs ov-small" style="top:230px;left:146px;width:55px">Natus error sit voluptatem accusantium doloremque laudantium, totam.</div>
  <div class="abs ov-small" style="top:243px;left:22px">• Lorem ipsum<br>• Dolor sit amet<br>• Incidunt</div>
  <div class="abs ov-small" style="top:243px;left:84px">• Lorem ipsum<br>• Dolor sit amet<br>• Incidunt</div>
  <div class="abs ov-small" style="top:243px;left:146px">• Lorem ipsum<br>• Dolor sit amet<br>• Incidunt</div>

  <div class="abs ov-band"></div>
  <div class="abs ov-marquee">* CO2 <span style="font-size:12px;vertical-align:middle">×</span> RNG ASSETS</div>
  <div class="abs ov-label" style="top:333px;left:0;width:227px;text-align:center">What we do</div>
  <p class="abs ov-quote">Lead the energy transition through partnerships with global businesses to help reduce their environmental footprint by producing renewable natural gas and other renewable products <u>LNG</u></p>
  <div class="abs" style="top:404px;left:0;width:227px;text-align:center;font-size:3px;font-weight:700">Dana Mirel<br><span style="font-weight:400;color:var(--grey)">President</span></div>

  <div class="ph" role="img" aria-label="Industrial pipework with a green leaf in front" style="left:65px;top:429px;width:95px;height:69px;background:linear-gradient(135deg,#1f3550,#2f6a82 50%,#3a9a4d)"></div>
  <div class="abs ov-card" style="left:22px;top:443px;width:57px;height:62px">
    <div style="font-family:Sora,sans-serif;font-size:5px;font-weight:600">Open Hours</div>
    <div class="ov-small" style="margin-top:2px;font-size:2.3px;line-height:3px">Visit our team during the hours listed below for site tours.</div>
    <div class="ov-small" style="margin-top:4px;font-size:2.3px;line-height:3.2px">• Mon–Fri: 8 AM – 6 PM<br>• Saturday: 9 AM – 4 PM<br>• Sunday: Closed</div>
  </div>
  <div class="abs" style="left:147px;top:436px;width:57px;height:64px;background:var(--blue);color:#fff;padding:14px 10px">
    <div style="font-family:Sora,sans-serif;font-size:5px;font-weight:500">Contact us</div>
    <div style="margin-top:3px;font-size:2.3px;line-height:3px;opacity:.85">Reach our project team for gas offtake and CO2 supply.</div>
    <div style="margin-top:5px;width:27px;height:8px;border:1px solid #fff;font-size:2px;text-align:center;line-height:6px">Contact Now</div>
  </div>

  <div class="abs ov-stats">
    <div class="ov-stat"><span>98</span><em>Projects</em></div>
    <div class="ov-stat"><span>65</span><em>People</em></div>
    <div class="ov-stat"><span>10</span><em>Years</em></div>
    <div class="ov-stat" style="border:0"><span>15</span><em>Offices</em></div>
  </div>

  <div class="ph" role="img" aria-label="Forest and power plant on a round island of earth against a blue sky" style="left:0;top:562px;width:227px;height:107px;background:linear-gradient(90deg,#3d8ef0,#7bb6f5 45%,#c9a36c 75%,#3f9450)"></div>
  <div class="abs" style="left:22px;top:606px;width:96px;font-family:Sora,sans-serif;font-size:5px;line-height:6px;font-weight:500">Today, we are solving the two most critical issues causing global climate change</div>

  <div class="abs ov-logos"><div><i></i></div><div><i style="width:6px;height:6px;border-radius:50%"></i></div><div><i></i></div><div><i style="width:8px;height:6px"></i></div><div><i></i></div><div><i style="width:6px;height:6px"></i></div></div>

  <div class="ph" role="img" aria-label="Large steel gas pipelines under a cloudy sky" style="left:11px;top:709px;width:100px;height:72px;background:linear-gradient(180deg,#9cc3ea,#d6dde4 55%,#7d8a78)"></div>
  <div class="abs ov-label" style="top:709px;left:128px;font-size:2.2px">Corvel RNG Projects</div>
  <div class="abs head" style="top:714px;left:128px;font-size:9.3px;line-height:9.5px;font-weight:500">Capture and<br>convert<br>methane</div>
  <div class="abs ov-small" style="top:760px;left:147px;width:67px;font-size:2.3px;line-height:3px">A powerful greenhouse gas, methane is captured at our island landfill sites. Since launch, our projects have kept thousands of tonnes of CO2 equivalent from reaching the atmosphere. The methane is treated and converted into RNG.</div>
  <div class="abs" style="top:789px;left:147px;width:34px;height:9px;background:var(--green);color:#fff;font-size:2.2px;text-align:center;line-height:9px">View all Projects</div>

  <div class="abs ov-label" style="top:817px;left:0;width:227px;text-align:center;font-size:2.2px">Helping companies achieve net-zero now</div>
  <div class="abs head" style="top:822px;left:0;width:227px;text-align:center;font-size:6px;line-height:6.6px;font-weight:500">Delivering excellence in<br>renewables, sustainability.</div>
  <div class="abs ov-faq" style="top:844px">
    <div class="row" style="border:0;padding-bottom:1px"><span>How is oil extracted?</span><span>↘</span></div>
    <div class="ov-small" style="font-size:2.2px;line-height:3px;padding-bottom:3px;border-bottom:1px solid #e1e4ea">Wells are drilled into underground reservoirs and pressure or pumps bring the oil up to the surface, where it is separated from water and gas before transport to processing sites nearby.</div>
    <div class="row"><span>What are upstream oil activities?</span><span>→</span></div>
    <div class="row"><span>What is offshore drilling?</span><span>→</span></div>
    <div class="row"><span>What is fracking in oil production?</span><span>→</span></div>
    <div class="row"><span>What is the role of pipelines?</span><span>→</span></div>
  </div>

  <div class="abs ov-blog"></div>
  <div class="abs ov-label" style="top:946px;left:21px;font-size:2.2px">Articles</div>
  <div class="abs head" style="top:952px;left:21px;font-size:9px;font-weight:500">Our blog</div>
  <div class="abs" style="top:958px;left:186px;font-size:2.6px">Read More →</div>
  <div class="ph" role="img" aria-label="Geothermal plant with steam on open land" style="left:21px;top:969px;width:58px;height:43px;background:linear-gradient(180deg,#c4d3e0,#a76e43)"></div>
  <div class="ph" role="img" aria-label="Industrial site with smoke stacks" style="left:84px;top:969px;width:58px;height:43px;background:linear-gradient(180deg,#cfd6de,#6f7670)"></div>
  <div class="ph" role="img" aria-label="Aerial view of a processing plant among green fields" style="left:147px;top:969px;width:57px;height:43px;background:linear-gradient(180deg,#a7c4de,#4f7b62)"></div>
  <div class="abs ov-h" style="top:1019px;left:21px;width:58px;font-size:3.6px;line-height:4.4px"><span class="ov-label" style="font-size:1.8px">Industry</span><br>Advancing technology for safer oil extraction</div>
  <div class="abs ov-h" style="top:1019px;left:84px;width:58px;font-size:3.6px;line-height:4.4px"><span class="ov-label" style="font-size:1.8px">Industry</span><br>Global oil industry’s role in sustainability</div>
  <div class="abs ov-h" style="top:1019px;left:147px;width:58px;font-size:3.6px;line-height:4.4px"><span class="ov-label" style="font-size:1.8px">Industry</span><br>Exploring innovation in modern oil production</div>
  <div class="abs ov-small" style="top:1033px;left:21px;font-size:1.9px">March 21, 2025 · 2 Comments</div>
  <div class="abs ov-small" style="top:1033px;left:84px;font-size:1.9px">March 21, 2025 · 4 Comments</div>
  <div class="abs ov-small" style="top:1033px;left:147px;font-size:1.9px">March 21, 2025 · 3 Comments</div>

  <div class="abs ov-cta"></div>
  <div class="abs head" style="top:1073px;left:22px;color:#fff;font-size:6.4px;line-height:7px;font-weight:500">Want to learn more about<br>the benefits of RNG?</div>
  <div class="abs" style="top:1079px;left:178px;width:27px;height:8px;background:#fff;font-size:2.2px;text-align:center;line-height:8px;font-weight:700">Contact Us</div>

  <div class="abs ov-foot"></div>
  <div class="abs ov-logo" style="top:1114px;left:22px;color:#cfd2da;font-size:2.8px"><i style="width:7px;height:7px"></i><span>Corvel<br>Renewables</span></div>
  <nav class="abs ov-nav" style="top:1117px;left:129px;color:#cfd2da;font-size:2.6px;gap:4px"><span>Home</span><span>About Us</span><span>Landfill Gas</span><span>LNG</span><span>RNG</span><span>CO2</span></nav>
  <div class="abs" style="top:1145px;left:22px;font-size:2.4px;line-height:3.4px;color:#aeb2bc">Calle Marea 14<br>Suite 2B<br>Bayview, PR<br>00000</div>
  <div class="abs" style="top:1145px;left:84px;font-size:2.4px;line-height:3.4px;color:#cfd2da"><b>+1 555 010 2569</b><br><u>contact@corvelmetharoutes.com</u></div>
  <div class="abs" style="top:1145px;left:178px;width:26px;text-align:right;font-size:2.4px;line-height:3.4px;color:#aeb2bc">Get fresh updates<br>Get in Touch</div>
  <div class="abs" style="top:1173px;left:22px;font-size:2.3px;color:#8e929c">Corvel Renewables © 2025. All rights reserved.</div>
  <div class="abs" style="top:1172px;left:171px;display:flex;gap:3px"><i style="width:5px;height:5px;border-radius:50%;background:#3a3c44;display:block"></i><i style="width:5px;height:5px;border-radius:50%;background:#3a3c44;display:block"></i><i style="width:5px;height:5px;border-radius:50%;background:#3a3c44;display:block"></i><i style="width:5px;height:5px;border-radius:50%;background:#3a3c44;display:block"></i></div>
</section>

<!-- ===== Home page, close view ===== -->
<main class="main">
  <nav class="nav"><span>Home</span><span>About Us</span><span>Landfill Gas</span><span>LNG</span><span>RNG</span><span>CO2</span></nav>
  <div class="brand"><i></i><span>Corvel<br>Renewables</span></div>
  <a class="btn-contact">Contact Us</a>
  <svg class="menu-dots" width="16" height="16" viewBox="0 0 16 16" fill="none" stroke="#222" stroke-width="1.2">
    <circle cx="2.5" cy="2.5" r="1.6"/><circle cx="8" cy="2.5" r="1.6"/><circle cx="13.5" cy="2.5" r="1.6"/>
    <circle cx="2.5" cy="8" r="1.6"/><circle cx="8" cy="8" r="1.6"/><circle cx="13.5" cy="8" r="1.6"/>
    <circle cx="2.5" cy="13.5" r="1.6"/><circle cx="8" cy="13.5" r="1.6"/><circle cx="13.5" cy="13.5" r="1.6"/>
  </svg>

  <div class="ph hero-art" role="img" aria-label="Refinery plant built inside a large green leaf, with a landfill site, forest and cooling tower on a slab of earth, and leaves flying around"></div>
  <h1 class="hero-title">Achieve<br><span class="g">NET-ZERO</span><br>Now</h1>
  <svg class="hero-arrow" width="20" height="36" viewBox="0 0 20 36" fill="none" stroke="#1c1f2a" stroke-width="2.4">
    <line x1="10" y1="0" x2="10" y2="33"/><polyline points="2,25 10,34 18,25"/>
  </svg>
  <div class="asterisk">*</div>
  <div class="hero-list" style="top:322px"><b>01.</b> Island Sourced<br>Waste-to-Energy</div>
  <div class="hero-list" style="top:397px"><b>02.</b> Renewable<br>Natural Gas</div>
  <div class="hero-list" style="top:471px"><b>03.</b> ESG positive<br>energy assets</div>

  <div class="welcome">WELCOME TO CORVEL RENEWABLES</div>
  <h2 class="intro">Transitioning The World To A Zero Carbon Future With Renewable Natural Gas</h2>

  <article class="service" style="left:95px">
    <div class="art" role="img" aria-label="Isometric line drawing of a landfill gas plant with storage tank and chimneys"></div>
    <h3>Landfill Gas-to-RNG &amp; Electricity Facilities</h3>
    <p>Natus error sit voluptatem accusantium doloremque laudantium, totam.</p>
    <ul><li>Lorem ipsum</li><li>Dolor sit amet</li><li>Incidunt</li></ul>
  </article>
  <article class="service" style="left:361px">
    <div class="art" role="img" aria-label="Isometric line drawing of two oil barrels"></div>
    <h3>Renewable Natural Gas Production</h3>
    <p>Natus error sit voluptatem accusantium doloremque laudantium, totam.</p>
    <ul><li>Lorem ipsum</li><li>Dolor sit amet</li><li>Incidunt</li></ul>
  </article>
  <article class="service" style="left:627px">
    <div class="art" role="img" aria-label="Isometric line drawing of a tanker truck" style="width:128px"></div>
    <h3>Advanced Waste Processing</h3>
    <p>Natus error sit voluptatem accusantium doloremque laudantium, totam.</p>
    <ul><li>Lorem ipsum</li><li>Dolor sit amet</li><li>Incidunt</li></ul>
  </article>

  <div class="foot-band"></div>
</main>
</body>
</html>
```